Exciting New Reseller Brand requires Website to WOW New clients to register.

We are a NEW online business called Trade Our Goods.

The Website is a simple concept, it looks to put Merchants (businesses that want their products resold) in touch with Resellers (people or businesses that want to resell that product).

The website acts as an online market place which looks to get Merchants to sign-up and pay to list their company and product as well as getting Resellers to sign-up to view potential Merchants they can get in touch with in the right industry or area to resell their products for (see attached slide-pack to explain packages)

Any type of Industry or Business can register themselves to get listed on Trade Our Goods to see either get their product/service resold or to look for products / services to reseller.

Trade Our Goods does not take any other monetary part in the business relationships other than to obtain money for the monthly website subscription.

We want a very simple website, so this project is for several pages:

Page 1) A really vibrant, exciting, image based homepage to get people to sign-up / register (see sites that we like in the project brief). Needs to be very clear that there are 2 customers and to sign up to join, build and earn!

Page 2) A page that describes the benefits and packages for Resellers.

Page 3) A page that describes the benefits and packages for Merchants.

Page 4) The Payment process pages, taking the customer through sign-up

Page 5) The Business Listings page, so when people search for a Merchant how this will be displayed.

We would really like an image based site and preferably parallax. We want it bright vibrant and to look like a social media site.

All necessary files / logos enclosed.

We would love to continue to work with the winning designer moving forward.

Many thanks and Good Luck.

Regards

Martin & Owen

Target Market(s)

Merchants, Suppliers, Vendors, Manufacturers, Distributors, Wholesalers, Affiliate programs, Franchisees, Reselers

Industry/Entity Type

Business

Number of Pages Required

5+ page

Requirements
Must have
• We love the following websites:
• 1) Like the top section, i.e. parallax image based: www.brightkitestudio.co.uk
• 2) Like the way the screen is split in 2, could be used to describe the 2 different customers we are after Merchants / Resellers: www.filevault-example.com/guide
• 3) Like the bright colours / full screen video split into 2 below top banner and the generally how simple the site is: www.harbourlinden.com.au
• 4) Love all of this site, simple, bold, Love the colours, the clear message and the infographics: http://www.velorin-example.com/swiftrider/faster

```html
<!DOCTYPE html>
<html lang="en">
<head>
<meta charset="utf-8">
<title>Trade Our Goods — Home</title>
<link rel="stylesheet" href="https://fonts.googleapis.com/css2?family=Montserrat:wght@300;400;600;700&family=Open+Sans:wght@400;600&display=swap">
<style>
  :root{
    --hero-dark:#2a2420;
    --hero-mid:#5a4a3c;
    --hero-warm:#7a6552;
    --hero-navy:#262b3a;
    --bar-bg:rgba(30,30,30,.55);
    --white:#ffffff;
    --merchant-blue:#3c8fd0;
    --merchant-blue-deep:#2f7cbd;
    --reseller-green:#93c83e;
    --reseller-green-deep:#82bb2c;
    --button-text:#555555;
    --arrow-bg:rgba(40,40,40,.6);
  }
  *{margin:0;padding:0;box-sizing:border-box}
  html,body{width:1200px;height:793px;overflow:hidden;background:var(--hero-dark)}
  body{position:relative;font-family:'Open Sans',sans-serif;color:var(--white)}

  .hero{position:absolute;left:0;top:0;width:1200px;height:588px;
    background:
      radial-gradient(ellipse at 30% 45%, rgba(40,44,66,.9) 0%, rgba(40,44,66,0) 45%),
      radial-gradient(ellipse at 75% 60%, rgba(150,130,110,.55) 0%, rgba(150,130,110,0) 50%),
      linear-gradient(100deg,var(--hero-dark) 0%,var(--hero-navy) 30%,var(--hero-mid) 60%,var(--hero-warm) 100%);}

  .top-bar{position:absolute;left:0;top:0;width:1200px;height:36px;background:var(--bar-bg);
    font-size:11.5px;display:flex;align-items:center}
  .contacts{position:absolute;left:112px;display:flex;align-items:center;gap:22px;white-space:nowrap}
  .contact{display:flex;align-items:center;gap:6px}
  .account{position:absolute;left:865px;display:flex;align-items:center;gap:6px;white-space:nowrap}
  .account .search{margin-left:14px;display:flex;align-items:center;gap:6px}
  .social{position:absolute;left:999px;display:flex;gap:5px}
  .social span{width:18px;height:18px;background:rgba(255,255,255,.35);border-radius:2px}

  .brand{position:absolute;left:112px;top:60px;display:flex;align-items:center;gap:10px;
    font-family:'Montserrat',sans-serif;font-weight:600;font-size:27px;letter-spacing:-.5px;white-space:nowrap}
  .brand .dot{width:50px;height:50px;border-radius:50%;background:var(--white)}

  .main-nav{position:absolute;top:80px;left:581px;display:flex;font-size:13.5px;white-space:nowrap}
  .main-nav a{color:var(--white);text-decoration:none;margin-right:29px;letter-spacing:.2px}
  .main-nav a:last-child{margin-right:0}

  .slide-arrow{position:absolute;top:245px;width:27px;height:97px;background:var(--arrow-bg);
    display:flex;align-items:center;justify-content:center}
  .slide-arrow.prev{left:0}
  .slide-arrow.next{right:0}

  .headline{position:absolute;top:218px;left:0;width:1200px;text-align:center;font-family:'Montserrat',sans-serif}
  .headline .light{display:block;font-weight:300;font-size:60px;line-height:70px;letter-spacing:-1px}
  .headline .bold{display:block;font-weight:700;font-size:56px;line-height:72px;letter-spacing:-1px}

  .scroll-down{position:absolute;left:576px;top:491px;width:48px;height:48px;border-radius:50%;
    background:rgba(60,60,60,.8);display:flex;align-items:center;justify-content:center}

  .audience{position:absolute;top:588px;width:600px;height:205px;text-align:center;font-family:'Montserrat',sans-serif}
  .audience.merchants{left:0;background:linear-gradient(160deg,var(--merchant-blue) 0%,var(--merchant-blue-deep) 100%)}
  .audience.resellers{left:600px;background:linear-gradient(160deg,var(--reseller-green) 0%,var(--reseller-green-deep) 100%)}
  .audience h2{font-weight:700;font-size:48px;line-height:54px;margin-top:40px;letter-spacing:-.5px}
  .audience p{font-weight:600;font-size:22.5px;line-height:28px;white-space:nowrap}
  .audience .cta{display:inline-block;margin-top:11px;width:137px;height:36px;line-height:36px;
    background:var(--white);color:var(--button-text);font-family:'Open Sans',sans-serif;font-size:13.5px;text-decoration:none}
</style>
</head>
<body>
  <div class="hero" role="img" aria-label="Photo of a man on a phone call working on a laptop outdoors on wooden steps"></div>

  <div class="top-bar">
    <span class="contacts">
      <span class="contact">
        <svg width="13" height="10" viewBox="0 0 13 10"><rect x=".5" y=".5" width="12" height="9" fill="none" stroke="#fff"/><path d="M.5 .5 6.5 5.5 12.5 .5" fill="none" stroke="#fff"/></svg>
        sales@example.com
      </span>
      <span class="contact">
        <svg width="8" height="12" viewBox="0 0 8 12"><path d="M2 1 Q0 6 2 11 L4 10 3 7 4.5 6 5 4 3 2Z" fill="none" stroke="#fff"/></svg>
        (555) 010-0145
      </span>
    </span>
    <span class="account">Sign In |
      <span class="search">
        <svg width="13" height="13" viewBox="0 0 13 13"><circle cx="7.5" cy="5.5" r="4.5" fill="none" stroke="#fff" stroke-width="1.3"/><path d="M4.3 8.7 1 12" stroke="#fff" stroke-width="1.5"/></svg>
        Search
      </span>
    </span>
    <span class="social"><span></span><span></span><span></span><span></span></span>
  </div>

  <div class="brand"><span class="dot"></span>Trade Our Goods</div>

  <nav class="main-nav">
    <a href="#">HOME</a><a href="#">MERCHANTS</a><a href="#">RESELLER</a><a href="#">PRICING</a><a href="#">FAQ'S</a><a href="#">CONTACT US</a>
  </nav>

  <div class="slide-arrow prev"><svg width="10" height="16" viewBox="0 0 10 16"><path d="M8 1 2 8 8 15" fill="none" stroke="#fff" stroke-width="1.6"/></svg></div>
  <div class="slide-arrow next"><svg width="10" height="16" viewBox="0 0 10 16"><path d="M2 1 8 8 2 15" fill="none" stroke="#fff" stroke-width="1.6"/></svg></div>

  <h1 class="headline"><span class="light">Building You Own</span><span class="bold">Virtual Sales Team</span></h1>

  <div class="scroll-down"><svg width="22" height="20" viewBox="0 0 22 20"><path d="M2 3 11 10 20 3M2 10 11 17 20 10" fill="none" stroke="#fff" stroke-width="2"/></svg></div>

  <section class="audience merchants">
    <h2>Merchants</h2>
    <p>Register To Build Your Virtual Sales Team</p>
    <a class="cta" href="#">Get started</a>
  </section>
  <section class="audience resellers">
    <h2>Reseller</h2>
    <p>Register To Start Earning Money</p>
    <a class="cta" href="#">Get started</a>
  </section>
</body>
</html>
```